Hal's Remedies Business Card Design Project

I need a business card designed for my pharmacy Hal's Remedies. I would like just the logo on one side, maybe with black background and white lettering. The other side I would also like to include my logo which is attached. Also, please include my name and the following information:
Hal Norwick Owner/Pharm D.
Business address is 7163 N Birch Rd Sioux Falls, SD 57291.
Phone number is 605-318-6027 and fax # is 605-318-6031.
my email address is hal@halsremedies.example.
My website is www.halsremedies.example.
My business hours are Monday-Friday 8am-7 pm. Saturday 8am-12 pm. Sunday Closed.
I would like the design to include my logo colors, black, white, and neon green. Silver may be added as a highlight. Thanks.
Pharmacy
See above in product description

```html
<!DOCTYPE html>
<html lang="en">
<head>
<meta charset="utf-8">
<title>Hal's Remedies – Business Card</title>
<link rel="stylesheet" href="https://fonts.googleapis.com/css2?family=Open+Sans:wght@400;700&family=Raleway:wght@300&family=Kumbh+Sans:wght@700&display=swap">
<style>
  :root {
    --page: #ffffff;
    --slate-deep: #1f2b37;
    --slate: #2c3c4d;
    --slate-light: #3d5163;
    --panel: #233241;
    --white: #ffffff;
    --neon: #9dc93b;
    --shadow: rgba(0, 0, 0, 0.35);
  }
  * { margin: 0; padding: 0; box-sizing: border-box; }
  html, body {
    width: 1200px; height: 1000px; overflow: hidden;
    background: var(--page);
  }
  .canvas { position: relative; width: 1200px; height: 1000px; overflow: hidden; }

  .card {
    position: absolute; overflow: hidden;
    box-shadow: 0 8px 10px -2px var(--shadow);
    color: var(--white);
    font-family: "Open Sans", sans-serif;
  }

  /* Front side */
  .card-front { left: 86px; top: 94px; width: 614px; height: 353px; }
  .facet-backdrop {
    position: absolute; inset: 0;
    background: linear-gradient(135deg, var(--slate-deep) 0%, var(--slate-light) 35%, var(--slate) 60%, var(--slate-deep) 100%);
  }
  .brand-row { position: absolute; left: 27px; top: 20px; display: flex; align-items: center; height: 102px; }
  .brand-dot { width: 26px; height: 26px; border-radius: 50%; background: var(--neon); margin: 0 60px 0 50px; }
  .brand-rule { width: 2px; height: 102px; background: var(--white); margin-right: 26px; }
  .brand-name { font-weight: 700; font-size: 47px; letter-spacing: -1.5px; color: var(--white); }

  .hours { position: absolute; left: 280px; top: 184px; width: 320px; height: 150px; }
  .hours-rule { position: absolute; left: 165px; top: 12px; width: 2px; height: 138px; background: var(--white); }
  .hours-col { position: absolute; top: 0; text-align: center; }
  .hours-col.days { left: 0; width: 165px; }
  .hours-col.times { left: 167px; width: 160px; }
  .hours-head { font-family: "Raleway", sans-serif; font-weight: 300; font-size: 28px; line-height: 36px; margin-bottom: 4px; }
  .hours-cell { font-size: 19px; line-height: 35px; }
  .hours-cell.closed { color: var(--neon); }

  /* Back side */
  .card-back { left: 425px; top: 476px; width: 596px; height: 343px; background: var(--panel); }
  .facet-strip {
    position: absolute; left: 0; top: 0; width: 220px; height: 343px;
    background: linear-gradient(160deg, var(--slate-deep) 0%, var(--slate-light) 40%, var(--slate) 70%, var(--slate-deep) 100%);
  }
  .back-brand { position: absolute; left: 14px; top: 150px; display: flex; align-items: center; gap: 10px; }
  .back-brand .brand-dot { width: 18px; height: 18px; margin: 0; }
  .back-brand .brand-name { font-size: 25px; letter-spacing: -0.5px; }

  .holder-name {
    position: absolute; left: 270px; top: 38px;
    font-family: "Kumbh Sans", sans-serif; font-weight: 700; font-size: 42px; color: var(--neon);
  }
  .contact-list { position: absolute; left: 266px; top: 120px; list-style: none; }
  .contact-item { position: relative; height: 46px; display: flex; align-items: center; }
  .contact-item svg { width: 30px; height: 30px; fill: var(--white); flex: none; }
  .contact-text { position: absolute; left: 75px; font-size: 18px; white-space: nowrap; }
  .contact-item.address .contact-text { left: 61px; font-size: 15px; }
</style>
</head>
<body>
<div class="canvas">

  <section class="card card-front" aria-label="Card front">
    <div class="facet-backdrop" role="img" aria-label="Low-poly faceted background in slate blue tones"></div>
    <div class="brand-row">
      <span class="brand-dot"></span>
      <span class="brand-rule"></span>
      <span class="brand-name">Hal's Remedies</span>
    </div>
    <div class="hours">
      <span class="hours-rule"></span>
      <div class="hours-col days">
        <div class="hours-head">Day</div>
        <div class="hours-cell">Monday-Friday</div>
        <div class="hours-cell">Saturday</div>
        <div class="hours-cell closed">Sunday</div>
      </div>
      <div class="hours-col times">
        <div class="hours-head">Timing</div>
        <div class="hours-cell">8am-7 pm</div>
        <div class="hours-cell">8am-12 pm</div>
        <div class="hours-cell closed">Closed</div>
      </div>
    </div>
  </section>

  <section class="card card-back" aria-label="Card back">
    <div class="facet-strip" role="img" aria-label="Low-poly faceted background in slate blue tones"></div>
    <div class="back-brand">
      <span class="brand-dot"></span>
      <span class="brand-name">Hal's Remedies</span>
    </div>

    <h1 class="holder-name">Hal Norwick</h1>
    <ul class="contact-list">
      <li class="contact-item">
        <svg viewBox="0 0 24 24" aria-hidden="true"><path d="M6.6 10.8a15.1 15.1 0 0 0 6.6 6.6l2.2-2.2c.3-.3.7-.4 1-.2 1.1.4 2.3.6 3.6.6.6 0 1 .4 1 1V20c0 .6-.4 1-1 1A17 17 0 0 1 3 4c0-.6.4-1 1-1h3.5c.6 0 1 .4 1 1 0 1.3.2 2.5.6 3.6.1.3 0 .7-.2 1z"/></svg>
        <span class="contact-text">605-318-6027</span>
      </li>
      <li class="contact-item">
        <svg viewBox="0 0 24 24" aria-hidden="true"><path d="M7 2h10v7H7zM8.5 4h7v1h-7zm0 2h7v1h-7zM3 10h18v12H3zm3 2c-.6 0-1 1-1 2h3c0-1-.4-2-1-2zm12 0c-.6 0-1 1-1 2h3c0-1-.4-2-1-2zm-9 1v2h6v-2zm-3 4v3h12v-3z"/></svg>
        <span class="contact-text">605-318-6031</span>
      </li>
      <li class="contact-item">
        <svg viewBox="0 0 24 24" aria-hidden="true"><path d="M2 5h20v1.2l-10 6.3L2 6.2zm0 3.5 10 6.2 10-6.2V19H2z"/></svg>
        <span class="contact-text">hal@halsremedies.example</span>
      </li>
      <li class="contact-item">
        <svg viewBox="0 0 24 24" aria-hidden="true"><path d="M12 6c3.9 0 7.4 1.5 10 4l-1.7 1.7A11.7 11.7 0 0 0 12 8.4c-3.2 0-6.2 1.3-8.3 3.3L2 10c2.6-2.5 6.1-4 10-4zm0 4.7c2.6 0 4.9 1 6.6 2.6l-1.7 1.7a7 7 0 0 0-9.8 0l-1.7-1.7c1.7-1.6 4-2.6 6.6-2.6zm0 4.6c1.3 0 2.4.5 3.3 1.3L12 19.9l-3.3-3.3c.9-.8 2-1.3 3.3-1.3z"/></svg>
        <span class="contact-text">www.halsremedies.example</span>
      </li>
      <li class="contact-item address">
        <svg viewBox="0 0 24 24" aria-hidden="true"><path d="M12 1.5a6.5 6.5 0 0 0-6.5 6.5c0 4.8 6.5 14.5 6.5 14.5S18.5 12.8 18.5 8A6.5 6.5 0 0 0 12 1.5zm0 9a2.5 2.5 0 1 1 0-5 2.5 2.5 0 0 1 0 5z"/></svg>
        <span class="contact-text">7163 N Birch Rd Sioux Falls, SD 57291</span>
      </li>
    </ul>
  </section>

</div>
</body>
</html>
```